Business card design needed

The company name is Wendale Architects. We are an architectural company based in Melbourne,Australia that has a mix of client base from health care, commercial office, aged care, multi-residential, single residential and retail. Design type is contemporary.

Suggest the base colours need to be black and white. Please leave an area on the back of the card available for handwritten notes.

Target Market(s)

Generally corporate, aged 30 to 65

Industry/Entity Type

Residential

Contact Information for Business Card

Wendale Architects
Mark Wendale
14 Pellow Street
Rosevale VIC 3071
T (03) 9512 4067
M 0438 617 295
E mw@wendalearc.com.au

Logo Text

WA

Logo styles of interest
Emblem Logo
Abstract Logo
Lettermark Logo
Requirements
Must have
• I am having trouble attaching a sketch so would really appreciate your effort to try the following brief.

Black and White (B&W)
Would like different card cutout profile. Logo Example, use the half circle curve of the G to form the left edge of the card with no margin. The A is to sit inside the G, connected to the G by its horizontal. The A has its cross bar and lower right leg removed. Card in black, text in white.

Back of card to be black text on white background with services provided.

Client Focused Service
Architecture and Design
Functional Planning
Town Planning
Feasability Studies
Contract Documentation
Contract Administration
Project Management

Simple elegant text, Ariel or similar
Nice to have
• Integrated logo and card cut-out.

Card base black on front, white on back
Should not have
• Too many colours
Fussy details

```html
<!DOCTYPE html>
<html lang="en">
<head>
<meta charset="utf-8">
<title>Wendale Architects – Business Card</title>
<link href="https://fonts.googleapis.com/css2?family=Jost:wght@300;400;500&display=swap" rel="stylesheet">
<style>
  :root {
    --stage: #1d1d1f;
    --card-dark: #262527;
    --card-light: #ffffff;
    --accent-blue: #2b3fa8;
    --text-light: #e6e6e6;
    --text-dark: #2c2c2c;
    --rule: #8a8a8a;
    --muted: #8c8c8c;
  }
  * { box-sizing: border-box; margin: 0; padding: 0; }
  html, body {
    width: 1200px; height: 900px; overflow: hidden;
    background: var(--stage);
    font-family: "Jost", "Futura", sans-serif;
  }
  .canvas {
    position: relative; width: 1200px; height: 900px;
  }
  .card {
    position: absolute; left: 220px; width: 760px; height: 380px;
  }
  /* Back of card: white, rounded right edge */
  .card--back {
    top: 50px;
    background: var(--card-light);
    border-radius: 0 190px 190px 0;
    padding: 48px 56px;
    color: var(--text-dark);
  }
  .brand {
    display: flex; align-items: center; gap: 14px;
  }
  .brand__dot {
    width: 34px; height: 34px; border-radius: 50%;
    border: 5px solid var(--accent-blue);
  }
  .brand__name {
    font-weight: 300; font-size: 30px; letter-spacing: 2px;
    text-transform: uppercase; color: var(--text-dark);
  }
  .services { margin-top: 26px; }
  .services__title {
    font-weight: 400; font-size: 24px; margin-bottom: 8px;
  }
  .services__list { list-style: none; }
  .services__item {
    font-weight: 300; font-size: 20px; line-height: 30px;
    position: relative; padding-left: 30px;
  }
  .services__item::before {
    content: ""; position: absolute; left: 4px; top: 12px;
    width: 8px; height: 8px; border-radius: 50%; background: var(--text-dark);
  }
  .notes-area {
    position: absolute; right: 190px; top: 90px; width: 200px;
  }
  .notes-area__line {
    height: 40px; border-bottom: 1px solid #dcdcdc;
  }

  /* Front of card: black, rounded left edge */
  .card--front {
    top: 470px;
    background: var(--card-dark);
    border-radius: 190px 0 0 190px;
    color: var(--text-light);
  }
  .mark-area {
    position: absolute; left: 40px; top: 40px; width: 300px; height: 300px;
    border-radius: 50%; border: 26px solid var(--accent-blue);
    display: flex; align-items: center; justify-content: center;
  }
  .mark-area__name {
    font-weight: 300; font-size: 28px; letter-spacing: 2px;
    color: var(--text-light); text-align: center; line-height: 1.2;
  }
  .contact {
    position: absolute; right: 56px; top: 46px; width: 330px;
    text-align: right;
  }
  .contact__name {
    font-weight: 400; font-size: 26px; color: var(--accent-blue);
    padding-bottom: 8px; border-bottom: 1px solid var(--rule);
  }
  .contact__list { list-style: none; padding: 10px 0; border-bottom: 1px solid var(--rule); }
  .contact__row {
    display: flex; justify-content: flex-end; align-items: center; gap: 12px;
    font-weight: 300; font-size: 20px; line-height: 28px;
  }
  .contact__icon { width: 16px; height: 16px; fill: var(--text-light); flex: none; }
  .contact__spacer { width: 16px; flex: none; }
  .wordmark {
    margin-top: 22px;
    font-weight: 300; font-size: 34px; letter-spacing: 3px;
    color: var(--accent-blue); line-height: 1.15;
  }
</style>
</head>
<body>
<main class="canvas">

  <section class="card card--back" aria-label="Card back">
    <div class="brand">
      <span class="brand__dot"></span>
      <span class="brand__name">Wendale Architects</span>
    </div>
    <div class="services">
      <h2 class="services__title">Client Focused Service</h2>
      <ul class="services__list">
        <li class="services__item">Architecture + Design</li>
        <li class="services__item">Functional Planning</li>
        <li class="services__item">Town Planning</li>
        <li class="services__item">Feasibility Studies</li>
        <li class="services__item">Contract Documentation</li>
        <li class="services__item">Contract Administration</li>
      </ul>
    </div>
    <div class="notes-area" aria-hidden="true">
      <div class="notes-area__line"></div>
      <div class="notes-area__line"></div>
      <div class="notes-area__line"></div>
      <div class="notes-area__line"></div>
    </div>
  </section>

  <section class="card card--front" aria-label="Card front">
    <div class="mark-area">
      <span class="mark-area__name">Wendale<br>Architects</span>
    </div>

    <div class="contact">
      <h1 class="contact__name">Mark Wendale</h1>
      <ul class="contact__list">
        <li class="contact__row">14 Pellow Street,
          <svg class="contact__icon" viewBox="0 0 16 16"><path d="M8 0a5.5 5.5 0 0 0-5.5 5.5C2.5 9.5 8 16 8 16s5.5-6.5 5.5-10.5A5.5 5.5 0 0 0 8 0zm0 7.5a2 2 0 1 1 0-4 2 2 0 0 1 0 4z"/></svg>
        </li>
        <li class="contact__row">Rosevale 3071<span class="contact__spacer"></span></li>
        <li class="contact__row">(03) 9512 4067
          <svg class="contact__icon" viewBox="0 0 16 16"><path d="M1 6c0-2 3-3.5 7-3.5S15 4 15 6v1h-3.5V5.5h-7V7H1zM3 8h10l1.5 6h-13z"/></svg>
        </li>
        <li class="contact__row">0438 617 295
          <svg class="contact__icon" viewBox="0 0 16 16"><path d="M4 0h8a1 1 0 0 1 1 1v14a1 1 0 0 1-1 1H4a1 1 0 0 1-1-1V1a1 1 0 0 1 1-1zm1 2v8h6V2zm3 10a1 1 0 1 0 0 2 1 1 0 0 0 0-2z"/></svg>
        </li>
        <li class="contact__row">mw@wendalearc.com
          <svg class="contact__icon" viewBox="0 0 16 16"><path d="M0 3h16v10H0zm1.5 1.2V12h13V4.2L8 9z"/></svg>
        </li>
      </ul>
      <p class="wordmark">Wendale Architects</p>
    </div>
  </section>

</main>
</body>
</html>
```